Wordpress Web Design & Coding for velnoragroup.ca

We need a website for a new investment company that is visually grabbing and vibrant. We would like to see a web page that displays trust, growth and confidence. Needs to be responsive and mobile friendly for all browsers and coded for both Android & IOS.

Open to the number of pages and menu items. I selected 4 but if you feel the layout would work better with less I am open to this. Need to sell the people (management team/related businesses) and then show where the invested money will be going (upcoming projects).

Company Info:

Velnora is an investment company put together by a group of seasoned business professionals who have come together to combine decades of success in the real estate development, management, financing and medical services. The company will be a full service company offering turn key solutions for medical professionals.

Vel-Nora will focus on providing a full range of services via a group of distinct companies to deliver newly emerging needs of the medical community. The end goal will be to create complete solutions for individuals in the medical community. Our group has experience and success with the conceptualization, construction and financing of medical and dental clinic spaces. Vel-Nora Group will be established to accommodate all areas of the development and creation of clinics for medical professionals from building construction to equipment financing and administrations.

You can mention these companies and take photos from their websites. You can also use stock photos.

Our construction partner:
https://382bld.com/projects/

Our equipment leasing partner:
https://www.pordiva.com/

Our Management Team and medical partners

Gil Parkes
https://www.mysoundpoise.ca/

Milos Vendraker
https://www.qrtdentalservices.com/about-us

PROPOSED PROJECTS (see attachment for details)
Hollowmere Business Park
Cresfield Business Park
Mt. Corwin Ridge Professional

Investors

Investment

Sans Serif

Must have
• Wordpress – must be both desktop and mobile friendly with fast page load speed
Ability to edit after ourselves in Wordpress
Attractive home page with logo etc.
Logo colours are: for the blue the pantone color is #0355a3
and for the green is #8cc63f

Sections, about us, what we do/services we provide, contact us

```html
<!DOCTYPE html>
<html lang="en">
<head>
<meta charset="utf-8">
<title>Vel-Nora Group</title>
<link href="https://fonts.googleapis.com/css2?family=Roboto:wght@300;400;500;700&display=swap" rel="stylesheet">
<style>
:root{
  --blue:#0355a3;
  --blue-dark:#023f7d;
  --blue-deep:#0a2c5c;
  --green:#8cc63f;
  --grey-bg:#efefef;
  --text:#444;
  --footer:#0b1a30;
  --footer-dark:#06101f;
  --white:#fff;
}
*{box-sizing:border-box;margin:0;padding:0}
html,body{width:1200px;height:2904px;overflow:hidden;background:var(--white)}
body{font-family:'Roboto',sans-serif;color:var(--text)}
section,header,footer{position:relative;width:1200px;overflow:hidden}
.abs{position:absolute}
.btn{position:absolute;display:flex;align-items:center;justify-content:center;background:var(--green);color:var(--white);font-weight:500;border-radius:30px;font-size:14px}
.wave{position:absolute}

/* header */
.site-header{height:70px;background:var(--white);z-index:3}
.brand{position:absolute;left:40px;top:0;width:160px;height:92px;background:var(--white);box-shadow:0 3px 8px rgba(0,0,0,.12);border-radius:0 0 6px 6px;display:flex;align-items:center;justify-content:center;gap:8px}
.brand-square{width:14px;height:14px;background:var(--green)}
.brand-name{font-weight:700;font-size:22px;color:var(--blue)}
.nav{position:absolute;left:320px;top:0;height:70px;display:flex;gap:34px;align-items:center;font-size:13px;color:#333}
.nav .active{color:var(--green);position:relative;height:70px;display:flex;align-items:center}
.nav .active::after{content:"";position:absolute;left:-8px;right:-8px;bottom:0;height:3px;background:var(--green)}
.call{position:absolute;left:890px;top:14px;display:flex;align-items:center;gap:10px}
.call-icon{width:40px;height:40px;border-radius:50%;background:var(--blue);display:flex;align-items:center;justify-content:center}
.call-num{font-size:19px;font-weight:700;color:var(--green);line-height:1}
.call-sub{font-size:11px;color:#555}

/* hero */
.hero{height:420px}
.hero-photo{position:absolute;inset:0;background:linear-gradient(100deg,#0b2b5c 0%,#16427e 40%,#0b2f63 100%)}
.hero-text{position:absolute;left:619px;top:72px;color:var(--white);width:420px}
.hero-text .pre{font-size:36px;font-weight:300}
.hero-text .title{font-size:38px;font-weight:700;color:var(--green);margin-top:2px}
.hero-text p{font-size:15px;line-height:26px;margin-top:22px}

/* about */
.about{height:390px;background:var(--grey-bg);margin-top:-1px}
.sec-title{font-size:24px;font-weight:400;color:var(--blue)}
.about p{position:absolute;left:138px;width:940px;font-size:12.5px;line-height:21px;color:#444}
.about b{color:#222}

/* what we do */
.services{height:556px;background:var(--white)}
.services-photo{position:absolute;left:0;right:0;top:0;bottom:0}
.services-lead{position:absolute;left:160px;top:245px;width:426px;text-align:center;color:var(--white);font-size:19px;line-height:28px;font-weight:300}
.card{position:absolute;background:var(--white);border-radius:8px;box-shadow:0 6px 18px rgba(0,0,0,.18);display:flex;flex-direction:column;align-items:center;justify-content:center;text-align:center;color:var(--blue);font-weight:500;font-size:16px;line-height:20px;gap:14px}

/* team */
.team{height:680px;background:var(--white)}
.tile{position:absolute;width:193px;height:153px}
.photo{background:linear-gradient(135deg,#7a8794,#4e5a66)}
.member{display:flex;flex-direction:column;align-items:center;justify-content:center;gap:10px;text-align:center}
.member .who{font-size:11px;font-weight:700;color:var(--blue)}
.member .co{font-size:18px;font-weight:400;color:#333}
.plus{width:18px;height:18px;border-radius:50%;background:var(--green);position:relative}
.plus::before,.plus::after{content:"";position:absolute;background:var(--white);left:50%;top:50%;transform:translate(-50%,-50%)}
.plus::before{width:9px;height:2px}
.plus::after{width:2px;height:9px}
.plan{background:var(--blue);color:var(--white);font-size:17px;line-height:24px;padding:0 20px;display:flex;align-items:center}

/* projects */
.projects{height:500px;background:var(--white)}
.project{position:absolute;top:143px;width:319px;height:292px;background:var(--white);box-shadow:0 4px 16px rgba(0,0,0,.12);border-radius:4px;text-align:center}
.project .img{position:absolute;left:12px;top:12px;right:12px;height:174px}
.project h3{position:absolute;top:200px;width:100%;font-size:16px;font-weight:700;color:var(--blue)}
.project .sub{position:absolute;top:226px;width:100%;font-size:11px;color:#666}
.project .plus{position:absolute;left:150px;top:256px}

/* footer */
.site-footer{height:232px;background:var(--footer);color:#d8dee8}
.foot-brand{position:absolute;left:154px;top:62px;display:flex;align-items:center;gap:8px}
.foot-brand .brand-name{color:var(--blue);font-size:24px}
.socials{position:absolute;left:166px;top:112px;display:flex;gap:6px}
.socials span{width:22px;height:22px;border-radius:3px}
.fcol{position:absolute;top:58px;font-size:12px}
.fcol h4{font-size:13px;font-weight:500;color:var(--white);margin-bottom:26px;letter-spacing:.3px}
.fcol li{list-style:none;margin-bottom:13px}
.contact li{display:flex;gap:10px;align-items:flex-start;line-height:18px;margin-bottom:9px}
.copy{height:56px;background:var(--footer-dark);color:#cfd6e0;font-size:11px;display:flex;align-items:center;justify-content:center}
</style>
</head>
<body>

<header class="site-header">
  <div class="brand"><span class="brand-square"></span><span class="brand-name">VEL-NORA</span></div>
  <nav class="nav">
    <span>Home</span><span class="active">About Us</span><span>What We Do</span><span>Our Projects</span><span>Contact Us</span>
  </nav>
  <div class="call">
    <div class="call-icon">
      <svg width="18" height="18" viewBox="0 0 24 24"><path fill="#fff" d="M6.6 10.8c1.4 2.8 3.8 5.1 6.6 6.6l2.2-2.2c.3-.3.7-.4 1-.2 1.1.4 2.3.6 3.6.6.6 0 1 .4 1 1V20c0 .6-.4 1-1 1C10.6 21 3 13.4 3 4c0-.6.4-1 1-1h3.5c.6 0 1 .4 1 1 0 1.3.2 2.5.6 3.6.1.3 0 .7-.2 1z"/></svg>
    </div>
    <div><div class="call-num">604-555-0192</div><div class="call-sub">Call us now!</div></div>
  </div>
</header>

<section class="hero">
  <div class="hero-photo" role="img" aria-label="Photo of a modern two-storey medical office building at dusk, tinted blue"></div>
  <svg class="wave" style="left:0;bottom:0" width="1200" height="60" viewBox="0 0 1200 60" preserveAspectRatio="none"><path d="M0 0 Q600 80 1200 0 L1200 60 L0 60Z" fill="#efefef"/></svg>
  <div class="hero-text">
    <div class="pre">Invest in</div>
    <div class="title">VEL-NORA Group</div>
    <p>Vel-Nora Group established to accommodate all areas of the development and creation of <b>clinics for medical professionals</b></p>
  </div>
  <div class="btn" style="left:619px;top:298px;width:134px;height:40px">About Us</div>
</section>

<section class="about">
  <div class="abs sec-title" style="left:138px;top:58px">ABOUT US</div>
  <svg class="wave" style="left:138px;top:94px" width="200" height="8" viewBox="0 0 200 8"><path d="M0 4 Q5 0 10 4 T20 4 T30 4 T40 4 T50 4 T60 4 T70 4 T80 4 T90 4 T100 4 T110 4 T120 4 T130 4 T140 4 T150 4 T160 4 T170 4 T180 4 T190 4 T200 4" fill="none" stroke="#8cc63f" stroke-width="1.5"/></svg>
  <p style="top:118px"><b>Velnora</b> is an investment company put together by a group of seasoned business professionals who have come together to combine decades of success in the real estate development, management, financing and medical services. The company will be a full service company offering turn key solutions for medical professionals.</p>
  <p style="top:196px"><b>Velnora</b> will focus on providing a full range of services via a group of distinct companies to deliver newly emerging needs of the medical community. The end goal will be to create complete solutions for individuals in the medical community. Our group has experience and success with the conceptualization, construction and financing of medical and dental clinic spaces. Vel-Nora Group will be established to accommodate all areas of the development and creation of clinics for medical professionals from building construction to equipment financing and administrations.</p>
  <div class="btn" style="left:138px;top:315px;width:272px;height:40px;font-size:13px">Our Management Team &amp; Partners</div>
</section>

<section class="services">
  <svg class="services-photo" width="1200" height="556" viewBox="0 0 1200 556" preserveAspectRatio="none" role="img" aria-label="Blue-tinted photo of the medical office building">
    <defs><linearGradient id="svcg" x1="0" y1="0" x2="1" y2="1"><stop offset="0" stop-color="#1a5ba6"/><stop offset="1" stop-color="#0355a3"/></linearGradient></defs>
    <path d="M0 20 Q600 -20 1200 20 L1200 520 Q600 580 0 520Z" fill="url(#svcg)"/>
  </svg>
  <div class="abs" style="left:0;width:1200px;top:50px;text-align:center;color:#fff;font-size:24px">WHAT WE DO</div>
  <svg class="wave" style="left:500px;top:88px" width="200" height="8" viewBox="0 0 200 8"><path d="M0 4 Q5 0 10 4 T20 4 T30 4 T40 4 T50 4 T60 4 T70 4 T80 4 T90 4 T100 4 T110 4 T120 4 T130 4 T140 4 T150 4 T160 4 T170 4 T180 4 T190 4 T200 4" fill="none" stroke="#8cc63f" stroke-width="1.5"/></svg>
  <div class="services-lead">Vel-Nora Group established to accommodate all areas of the development and creation of clinics for medical professionals</div>
  <div class="btn" style="left:297px;top:350px;width:234px;height:40px;font-size:13px">Our Upcoming Projects</div>

  <div class="card" style="left:649px;top:189px;width:213px;height:173px">
    <svg width="54" height="60" viewBox="0 0 54 60" fill="none" stroke="#8cc63f" stroke-width="2"><path d="M10 58V14M22 58V14M10 20h12M10 32h12M10 44h12M4 8h46M16 2v6M44 8v18M38 26h12v8H38z"/><path d="M4 58h30"/></svg>
    <span>Medical Building<br>Construction</span>
  </div>
  <div class="card" style="left:879px;top:118px;width:206px;height:173px">
    <svg width="60" height="46" viewBox="0 0 60 46" fill="none" stroke="#8cc63f" stroke-width="2"><rect x="2" y="8" width="40" height="22" rx="2"/><circle cx="22" cy="19" r="6"/><ellipse cx="48" cy="30" rx="10" ry="4"/><path d="M38 30v6c0 2 4 4 10 4s10-2 10-4v-6M38 36v6c0 2 4 4 10 4s10-2 10-4v-6"/></svg>
    <span>Equipment<br>Financing</span>
  </div>
  <div class="card" style="left:879px;top:307px;width:206px;height:174px">
    <svg width="56" height="52" viewBox="0 0 56 52" fill="none" stroke="#8cc63f" stroke-width="2"><rect x="2" y="8" width="52" height="42" rx="3"/><path d="M2 18h52M14 2v12M42 2v12M16 40V28h8v12M32 40V24h8v16"/></svg>
    <span>Construction<br>Administrations</span>
  </div>
</section>

<section class="team">
  <div class="abs sec-title" style="left:0;width:1200px;top:72px;text-align:center">OUR MANAGEMENT TEAM</div>
  <svg class="wave" style="left:500px;top:110px" width="200" height="8" viewBox="0 0 200 8"><path d="M0 4 Q5 0 10 4 T20 4 T30 4 T40 4 T50 4 T60 4 T70 4 T80 4 T90 4 T100 4 T110 4 T120 4 T130 4 T140 4 T150 4 T160 4 T170 4 T180 4 T190 4 T200 4" fill="none" stroke="#8cc63f" stroke-width="1.5"/></svg>

  <div class="tile photo" style="left:192px;top:153px" role="img" aria-label="Portrait of Dane Holloway"></div>
  <div class="tile member" style="left:386px;top:153px"><div class="who">Dane Holloway</div><div class="co">PORDIVA</div><div class="plus"></div></div>

  <div class="tile photo" style="left:0;top:305px" role="img" aria-label="Portrait of Milos Vendraker outdoors"></div>
  <div class="tile member" style="left:192px;top:305px"><div class="who">Milos Vendraker</div><div class="co">QRT</div><div class="plus"></div></div>
  <div class="tile plan" style="left:386px;top:305px">Select Your<br>Investment Plan</div>
  <div class="abs" style="left:578px;top:318px;width:622px;height:126px;background:linear-gradient(90deg,#b7c0c9 0%,#8e9cab 33%,#a9b2bb 66%,#c7bfb2 100%)" role="img" aria-label="Strip of project building and clinic interior photos"></div>

  <div class="tile member" style="left:0;top:458px"><div class="who">Dr. Gil Parkes</div><div class="co">soundpoise</div><div class="plus"></div></div>
  <div class="tile photo" style="left:192px;top:458px" role="img" aria-label="Portrait of Dr. Gil Parkes"></div>

  <p class="abs" style="left:620px;top:478px;width:360px;font-size:12px;line-height:20px;color:#555">Lorem ipsum dolor sit amet, consectetur adipiscing elit. Ut elit tellus, luctus nec ullamcorper mattis, pulvinar dapibus leo.</p>
  <div class="btn" style="left:800px;top:545px;width:175px;height:34px;font-size:12px">Upcoming Projects</div>
</section>

<section class="projects">
  <svg class="wave" style="left:0;top:0" width="1200" height="232" viewBox="0 0 1200 232" preserveAspectRatio="none"><path d="M0 30 Q600 -10 1200 30 L1200 232 L0 232Z" fill="#0355a3"/></svg>
  <div class="abs" style="left:0;width:1200px;top:48px;text-align:center;color:#fff;font-size:24px">UPCOMING PROJECTS</div>
  <svg class="wave" style="left:500px;top:86px" width="200" height="8" viewBox="0 0 200 8"><path d="M0 4 Q5 0 10 4 T20 4 T30 4 T40 4 T50 4 T60 4 T70 4 T80 4 T90 4 T100 4 T110 4 T120 4 T130 4 T140 4 T150 4 T160 4 T170 4 T180 4 T190 4 T200 4" fill="none" stroke="#8cc63f" stroke-width="1.5"/></svg>

  <div class="project" style="left:102px">
    <div class="img" style="background:linear-gradient(135deg,#c9c1b4,#7d7468)" role="img" aria-label="Clinic reception interior"></div>
    <h3>Hollowmere Business Park</h3><div class="sub">Office and light industrial building project</div><div class="plus"></div>
  </div>
  <div class="project" style="left:440px">
    <div class="img" style="background:linear-gradient(180deg,#5f8fd0 0%,#9fb9dc 50%,#6f6f6f 100%)" role="img" aria-label="Rendering of a business park building"></div>
    <h3>Cresfield Business Park</h3><div class="sub">Cresfield, British Columbia</div><div class="plus"></div>
  </div>
  <div class="project" style="left:777px">
    <div class="img" style="background:linear-gradient(180deg,#6c9bd6 0%,#d9dde2 45%,#8d96a0 100%)" role="img" aria-label="Professional office building exterior"></div>
    <h3>Mt. Corwin Ridge Professional</h3><div class="sub">Professional Services Building</div><div class="plus"></div>
  </div>
</section>

<footer>
  <div class="site-footer" style="position:relative">
    <div class="foot-brand"><span class="brand-square"></span><span class="brand-name">VEL-NORA</span></div>
    <div class="socials"><span style="background:#3b5998"></span><span style="background:#1da1f2"></span><span style="background:#d62a2a"></span></div>
    <div class="fcol" style="left:360px"><h4>PARTNERS</h4><ul><li>382 Builders</li><li>Pordiva Equipment Leasing</li><li>Sound Poise</li><li>QRT Dental Services</li></ul></div>
    <div class="fcol" style="left:608px"><h4>RESOURCES</h4><ul><li>Home</li><li>About Us</li><li>Projects</li><li>Contact Us</li></ul></div>
    <div class="fcol contact" style="left:858px"><h4>CONTACTS</h4><ul>
      <li><svg width="10" height="14" viewBox="0 0 10 14"><path d="M5 0a5 5 0 0 0-5 5c0 4 5 9 5 9s5-5 5-9a5 5 0 0 0-5-5zm0 7a2 2 0 1 1 0-4 2 2 0 0 1 0 4z" fill="#8cc63f"/></svg><span>Lorem ipsum dolor sit amet,<br>consectetur adipiscing elit</span></li>
      <li><svg width="12" height="12" viewBox="0 0 24 24"><path fill="#8cc63f" d="M6.6 10.8c1.4 2.8 3.8 5.1 6.6 6.6l2.2-2.2c.3-.3.7-.4 1-.2 1.1.4 2.3.6 3.6.6.6 0 1 .4 1 1V20c0 .6-.4 1-1 1C10.6 21 3 13.4 3 4c0-.6.4-1 1-1h3.5c.6 0 1 .4 1 1 0 1.3.2 2.5.6 3.6.1.3 0 .7-.2 1z"/></svg><span>604-555-0177</span></li>
      <li><svg width="12" height="10" viewBox="0 0 12 10"><rect width="12" height="10" rx="1" fill="#8cc63f"/><path d="M0 1l6 4 6-4" stroke="#0b1a30" fill="none"/></svg><span>info@velnoragroup.ca</span></li>
    </ul></div>
  </div>
  <div class="copy">Copyright © 2020 VEL-NORA Group. All rights reserved.</div>
</footer>

</body>
</html>
```